Kerno Solutions: searching for a flyer to trow in letterboxes for properties we are interested in

Hello ,

Introduction:
We are a company based in Luxembourg called "Kerno Solutions". We are specialized in buying properties on which we develop and build constructions before selling them.

Informations for the flyer:
We need a flyer to trow into the letter boxes of property owners letting them know that we are interested in buying their property, if they are interested they can give us a call.

The text for the flyer/letter is in the attachment called >>2020-03-11_KS_Text for flyer,letter there might be slight changes<<.

We need to look competent, professional and financially stable.

The flyer needs to be short and not over welling with information otherwise it will land in the trash.

We have decided that we don't want real pictures on the flyer, but shapes of any kind, blue prints, drawings are fine.

Format should be in DIN A4. We plan to print the flyer on both sides in two different languages, in other words the design will be the same on both sides only the text will be in a different language.

I also added our current logo and here is the design of the website that is under construction at the moment http://www.kernosolutions-example.lu/. The logo's color can be changed into a different blue or uni color (all white or all black).
Updates

Hi, First time user the howl thing started faster as expected. Furthermore, I need to catch my boss to discust the project with him and he is on a lot of meetings. Please give us a little bit more time. Thanks

Target Market(s)

Property owners

Requirements
Must have
• email, phone number, tax number (RCS), Tax number , matriculation and address.
see word file in attachment for information
Nice to have
• Our company logo, in one form or an other, you can be creative, the logo is in the attachment.
Should not have
• Real pictures

```html
<!DOCTYPE html>
<html lang="fr">
<head>
<meta charset="utf-8">
<title>Kerno Solutions – Courrier</title>
<link href="https://fonts.googleapis.com/css2?family=Carlito:wght@400;700&family=Barlow+Condensed:wght@600&display=swap" rel="stylesheet">
<style>
  :root {
    --sky: #3eaee0;
    --ocean: #0b6a98;
    --deep: #034a6d;
    --navy: #03344f;
    --ink: #1a1a1a;
    --brand: #0e6a9c;
    --paper: #ffffff;
    --mark: #6f9bb5;
  }
  * { margin: 0; padding: 0; box-sizing: border-box; }
  html, body { width: 848px; height: 1200px; overflow: hidden; background: var(--paper); }
  .letter {
    position: relative;
    width: 848px;
    height: 1200px;
    background: var(--paper);
    font-family: "Carlito", "Calibri", sans-serif;
    color: var(--ink);
    overflow: hidden;
  }
  .band-top {
    position: absolute;
    left: 340px;
    top: 0;
    width: 508px;
    height: 60px;
    background: linear-gradient(90deg, var(--navy) 0%, var(--ocean) 55%, var(--sky) 100%);
    clip-path: polygon(0 0, 100% 0, 100% 45%, 20% 100%);
  }
  .band-bottom {
    position: absolute;
    left: 0;
    top: 975px;
    width: 848px;
    height: 225px;
    background: linear-gradient(160deg, var(--sky) 0%, var(--ocean) 35%, var(--deep) 65%, var(--navy) 100%);
    clip-path: polygon(0 35%, 100% 0, 100% 100%, 0 100%);
  }
  .brand {
    position: absolute;
    left: 88px;
    top: 248px;
    display: flex;
    align-items: center;
    gap: 12px;
  }
  .brand-square { width: 32px; height: 32px; background: var(--brand); }
  .brand-name {
    font-family: "Barlow Condensed", "Carlito", sans-serif;
    font-weight: 600;
    font-size: 34px;
    letter-spacing: 0.5px;
    color: var(--ink);
    line-height: 1;
  }
  .body-text {
    position: absolute;
    left: 88px;
    top: 390px;
    width: 665px;
    font-size: 18.5px;
    line-height: 19.5px;
  }
  .body-text p { margin-bottom: 20px; }
  .body-text .spaced { line-height: 26px; margin-top: -3px; }
  .body-text .closing { margin-bottom: 40px; }
  .body-text strong { font-weight: 700; }
  .contacts {
    position: absolute;
    left: 92px;
    top: 802px;
    list-style: none;
    font-size: 18.5px;
  }
  .contacts li { display: flex; align-items: center; height: 29.5px; }
  .contacts svg { width: 20px; height: 20px; margin-right: 11px; flex: none; }
  .footer-mark {
    position: absolute;
    left: 657px;
    top: 1138px;
    font-family: "Barlow Condensed", "Carlito", sans-serif;
    font-weight: 600;
    font-size: 16px;
    color: var(--mark);
    letter-spacing: 0.3px;
  }
</style>
</head>
<body>
<main class="letter">
  <div class="band-top" role="img" aria-label="Bandeau décoratif bleu en haut de page"></div>
  <div class="band-bottom" role="img" aria-label="Bandeau décoratif bleu en bas de page"></div>

  <div class="brand">
    <span class="brand-square"></span>
    <span class="brand-name">KERNO SOLUTIONS</span>
  </div>

  <section class="body-text">
    <p>Madame, Monsieur,</p>
    <p>Ce courrier vous a été adressé, car votre propriété a attiré notre attention.<br>
       Nous souhaiterions discuter avec vous de son éventuel rachat par notre société.</p>
    <p>En cas d’accord, nous vous assurons une décision rapide, un paiement garanti,<br>
       et zéro frais d’intermédiaire.</p>
    <p class="spaced">En attendant de vos nouvelles, nous restons à votre entière disposition pour tout<br>renseignement.</p>
    <p class="closing">Salutations distinguées,</p>
    <p>L’équipe de <strong>Kerno Solutions</strong></p>
  </section>

  <ul class="contacts">
    <li>
      <svg viewBox="0 0 24 24" fill="none" stroke="var(--brand)" stroke-width="2.2"><path d="M12 22s7-7.2 7-12.5A7 7 0 0 0 5 9.5C5 14.8 12 22 12 22z"/><circle cx="12" cy="9.5" r="2.6"/></svg>
      17 rue des Tilleuls, L-3390 Norvange
    </li>
    <li>
      <svg viewBox="0 0 24 24" fill="none" stroke="var(--brand)" stroke-width="2"><rect x="2.5" y="5.5" width="19" height="13" rx="1.5"/><path d="M3 6.5l9 7 9-7"/></svg>
      info@kernosolutions-example.lu
    </li>
    <li>
      <svg viewBox="0 0 24 24" fill="var(--brand)"><path d="M6.6 3.5l3 3.3-1.8 2.4c1.2 2.6 3.3 4.7 5.9 5.9l2.4-1.8 3.3 3-1.6 3.2C11 19.3 4.7 13 4.3 5.1z"/><path d="M14 3a7 7 0 0 1 7 7" fill="none" stroke="var(--brand)" stroke-width="1.8"/><path d="M14 6.5a3.5 3.5 0 0 1 3.5 3.5" fill="none" stroke="var(--brand)" stroke-width="1.8"/></svg>
      691 000 473
    </li>
  </ul>

  <div class="footer-mark">KERNO SOLUTIONS</div>
</main>
</body>
</html>
```